Modern Website Design for PollBeacon – CX & Loyalty SaaS Platform

We need a modern, professional, and responsive website design for our B2B SaaS platform, PollBeacon. We help companies collect real-time customer feedback, analyze insights, and improve loyalty — combining a powerful CX platform with expert consulting services. The website should clearly communicate who we are and what we offer within the first impression. It should balance data-driven visuals such as dashboards, analytics, and charts with a human, approachable feel. The design must include at least six key pages: Homepage, Product/Services, About, Blog/Resources, Contact/Demo, and Pricing. It should be conversion-focused with clear calls-to-action that encourage visitors to request a demo or contact us. The site must be fully responsive across desktop, tablet, and mobile. It should support multiple languages, starting with English and Danish. Most importantly, the delivery must be a final WordPress website, ready to go live, not just design files.

Target Market(s)

Our target market is medium-to-large B2B organizations. The primary audience includes CX leaders, executives, and managers in customer success and service who want to measure loyalty, understand customer insights, and improve retention.

Industry/Entity Type

Technology / SaaS / Customer Experience

Coding

Coded - Design and coding required

Number of Pages Required

5+ page

Font styles to use
Sans Serif

Requirements
Must have
• The project must deliver a final WordPress website that is fully responsive across all devices. The design should be clean, modern, and SaaS-inspired, with clear calls-to-action on every page. It must also support English and Danish, with a visible language toggle. The site should include visuals of dashboards and analytics that reflect data-driven insights. It must feature sections for case studies or testimonials to build trust. The copywriting should be SEO-friendly, and the design should include smooth animations or hover effects that add polish without making the website feel heavy.
Should not have
• Cluttered layouts, or generic stock photos such as handshakes

```html
<!DOCTYPE html>
<html lang="en">
<head>
<meta charset="utf-8">
<title>PollBeacon – Customer Experience Platform</title>
<link href="https://fonts.googleapis.com/css2?family=Lexend:wght@400;500;600;700&family=Poppins:wght@400;500;600&family=Playfair+Display:ital,wght@1,500&display=swap" rel="stylesheet">
<style>
:root{
  --blue:#1f5aae;
  --blue-dark:#173f86;
  --orange:#ef4b1f;
  --ink:#12151f;
  --muted:#4a5063;
  --hero-bg:#e9edf9;
  --soft-bg:#eef1fa;
  --navy:#0f1632;
  --line:#d7dcec;
  --white:#ffffff;
}
*{margin:0;padding:0;box-sizing:border-box}
html,body{width:1200px;height:4839px;overflow:hidden}
body{font-family:"Poppins",sans-serif;color:var(--ink);background:var(--white);position:relative}
.abs{position:absolute}
h1,h2,h3,h4{font-family:"Lexend",sans-serif}
.btn{position:absolute;display:flex;align-items:center;justify-content:center;border-radius:30px;font-family:"Lexend",sans-serif;font-size:11.5px;font-weight:500;letter-spacing:.3px;text-transform:uppercase;transition:transform .2s}
.btn:hover{transform:translateY(-2px)}
.btn-primary{background:linear-gradient(90deg,var(--blue),var(--orange));color:var(--white)}
.btn-outline{border:1.5px solid var(--blue-dark);color:var(--ink);background:var(--white)}
.section{position:absolute;left:0;width:1200px}
.center{text-align:center;left:0;width:1200px}
.sec-title{font-size:36px;font-weight:600;letter-spacing:.5px;text-transform:uppercase;color:var(--ink)}
.sec-sub{font-size:12.5px;color:var(--muted);line-height:24px}

/* header / hero */
.hero{top:0;height:798px;background:linear-gradient(180deg,#eef1fb 0%,var(--hero-bg) 100%)}
.brand{position:absolute;display:flex;align-items:center;gap:8px;font-family:"Lexend",sans-serif;font-weight:700;color:var(--blue-dark)}
.brand .mark{width:14px;height:14px;background:var(--orange);border-radius:3px}
.nav{position:absolute;left:376px;top:35px;display:flex;gap:19px;font-family:"Lexend",sans-serif;font-size:12px;font-weight:500;color:var(--ink)}
.lang{position:absolute;left:1014px;top:35px;font-family:"Lexend",sans-serif;font-size:12px;font-weight:600}
.lang span{color:#9aa3bb;font-weight:400}
.hero-title{top:140px;font-size:44px;font-weight:600;line-height:52px;color:var(--ink)}
.hero-title .accent{color:var(--orange)}
.hero-title .script{font-family:"Playfair Display",serif;font-style:italic;font-weight:500;color:var(--blue);text-decoration:underline;text-decoration-thickness:2px;text-underline-offset:6px}
.hero-sub{top:262px;font-size:15px;line-height:23px;color:#2b3042}

/* dashboard */
.dash{position:absolute;left:297px;top:413px;width:606px;height:413px;background:var(--white);border-radius:18px;border:6px solid #dfe5f7;box-shadow:0 20px 40px rgba(31,90,174,.12);overflow:hidden;font-family:"Poppins",sans-serif}
.dash .side{position:absolute;left:0;top:0;width:118px;height:100%;border-right:1px solid #eef0f6}
.dash .side .brand{left:22px;top:22px;font-size:11px}
.dash .side .brand .mark{width:7px;height:7px}
.dash .menu{position:absolute;left:12px;top:88px;width:96px}
.dash .menu div{font-size:7px;color:#6b7189;padding:0 10px;height:22px;line-height:22px;border-radius:4px}
.dash .menu .on{background:var(--blue);color:var(--white)}
.dash .logout{position:absolute;left:22px;bottom:20px;font-size:7px;color:#6b7189}
.dash .search{position:absolute;left:135px;top:14px;width:160px;height:14px;border-radius:7px;background:#f3f5fa;font-size:5.5px;color:#9aa0b4;padding-left:8px;line-height:14px}
.dash .user{position:absolute;right:16px;top:12px;display:flex;align-items:center;gap:5px;font-size:6px;font-weight:600}
.dash .user i{width:12px;height:12px;border-radius:50%;background:#c5cbe0;display:block}
.stat{position:absolute;top:52px;width:110px;height:44px}
.stat .lbl{font-size:6px;color:#7a8097;display:flex;align-items:center;gap:4px}
.stat .lbl i{width:9px;height:9px;border-radius:50%;display:block}
.stat .val{font-size:12px;font-weight:600;margin-top:6px}
.stat .val em{font-style:normal;font-size:5px;background:#dff3e6;color:#2b9a55;padding:1px 3px;border-radius:3px;margin-left:4px;vertical-align:middle}
.chart-card{position:absolute;left:135px;top:112px;width:280px;height:168px}
.chart-card .t{font-size:6px;color:#7a8097}
.chart-card .v{font-size:12px;font-weight:500;margin-top:4px}
.promo{position:absolute;left:428px;top:118px;width:150px;height:162px;background:var(--blue);border-radius:8px;color:var(--white);padding:14px 14px}
.promo .tag{display:inline-block;font-size:5px;background:rgba(255,255,255,.25);padding:2px 6px;border-radius:6px}
.promo .h{font-size:9px;font-weight:600;line-height:12px;margin-top:10px}
.promo .p{font-size:5.5px;line-height:8px;opacity:.8;margin-top:10px}
.promo .b{position:absolute;left:14px;bottom:18px;width:122px;height:16px;border-radius:8px;background:var(--white);color:var(--blue);font-size:6px;font-weight:600;text-align:center;line-height:16px}
.panel{position:absolute;top:292px;height:115px;border-top:1px solid #eef0f6;padding-top:10px}
.panel .t{font-size:7px;font-weight:600}
.act{display:flex;gap:6px;margin-top:9px;font-size:5.5px;line-height:8px;color:#4a5063}
.act i{width:10px;height:10px;border-radius:50%;flex:none;display:block}
.inv{width:100%;border-collapse:collapse;margin-top:8px;font-size:5px;color:#4a5063}
.inv td{padding:5px 2px;border-bottom:1px solid #f0f2f7}
.inv .pill{font-size:4.5px;padding:1px 4px;border-radius:4px}

/* trusted */
.trusted-title{top:898px;font-size:22px;font-weight:600;letter-spacing:.5px}
.partners{position:absolute;left:150px;top:958px;display:flex;gap:15px}
.partner{width:141px;height:75px;border:1px solid var(--line);border-radius:10px;background:var(--white);display:flex;align-items:center;justify-content:center;gap:7px;font-family:"Lexend",sans-serif;font-weight:600;font-size:15px;color:#1d2438;box-shadow:0 4px 10px rgba(20,30,70,.05)}
.partner i{width:16px;height:16px;border-radius:50%;background:var(--blue);display:block}

/* features */
.feat-title{top:1124px}
.feat-sub{top:1184px}
.fcard{position:absolute;width:287px;height:214px;background:var(--white);border-radius:12px;box-shadow:0 6px 22px rgba(20,40,100,.10);text-align:center;padding:20px 18px 0;transition:transform .25s}
.fcard:hover{transform:translateY(-4px)}
.fcard svg{width:66px;height:62px}
.fcard h3{font-size:17px;font-weight:600;margin-top:14px}
.fcard p{font-size:12px;line-height:23px;color:#2b3042;margin-top:6px}

/* about */
.about{top:1906px;height:588px;background:linear-gradient(180deg,#e8ecf8,#eef1fa)}
.about-photo{position:absolute;left:103px;top:1972px;width:498px;height:422px;clip-path:polygon(50% 0,100% 50%,50% 100%,0 50%);background:linear-gradient(135deg,#c7ccd6,#6c7688 55%,#3a4353)}
.an-card{position:absolute;left:466px;top:2073px;width:139px;height:149px;background:var(--white);border-radius:8px;box-shadow:0 8px 20px rgba(0,0,0,.12);padding:34px 12px 0}
.an-card .t{font-family:"Lexend",sans-serif;font-size:12px;font-weight:500}
.an-card .p{font-size:12px;color:var(--blue);font-weight:500;margin-top:2px}
.an-badge{position:absolute;left:446px;top:2058px;width:40px;height:40px;border-radius:50%;background:var(--orange);border:4px solid var(--white)}
.rating{position:absolute;left:357px;top:2295px;width:225px;height:46px;background:var(--white);border-radius:23px;box-shadow:0 6px 16px rgba(0,0,0,.1);display:flex;align-items:center;padding-left:8px;gap:0}
.rating i{width:26px;height:26px;border-radius:50%;border:2px solid var(--white);display:block;margin-right:-8px}
.rating .txt{margin-left:16px}
.rating .stars{color:#f5a623;font-size:12px;letter-spacing:1px}
.rating .small{font-size:7.5px;color:#3a9a55}
.rating .small b{color:var(--ink);font-weight:500}
.about-kicker{left:682px;top:2024px;font-family:"Lexend",sans-serif;font-size:16px;font-weight:600;color:var(--orange)}
.about-title{left:678px;top:2046px;font-size:38px;font-weight:600}
.about-text{left:672px;top:2108px;width:400px;font-size:12.5px;line-height:20.5px;color:#2b3042}
.about-text p+p{margin-top:9px}

/* why */
.why-title{top:2572px}
.why-sub{top:2624px}
.why-item{position:absolute;font-family:"Lexend",sans-serif;font-size:15.5px;font-weight:500;line-height:21px}
.why-icon{position:absolute;width:68px;height:68px;border-radius:50%;display:flex;align-items:center;justify-content:center;border:4px solid #dfe5f7}
.why-icon.b{background:var(--blue)}
.why-icon.o{background:var(--orange);border-color:#fbe0d7}

/* testimonials */
.testi{top:3183px;height:720px;background:linear-gradient(180deg,#f5f7fd,#e9edf9)}
.testi-title{top:3268px}
.testi-sub{top:3322px}
.tcard{position:absolute;top:3375px;width:289px;background:var(--white);border-radius:10px;box-shadow:0 6px 20px rgba(20,40,100,.08);padding:20px 16px 24px}
.tcard .head{display:flex;align-items:center;gap:12px;padding-bottom:16px;border-bottom:1px solid #eceef5}
.tcard .av{width:46px;height:46px;border-radius:50%;color:var(--white);font-family:"Lexend",sans-serif;font-size:18px;display:flex;align-items:center;justify-content:center;flex:none}
.tcard .n{font-family:"Lexend",sans-serif;font-size:14px;font-weight:500}
.tcard .c{font-size:10.5px;color:#5a6076}
.tcard .stars{color:var(--orange);font-size:15px;letter-spacing:3px;margin-top:14px}
.tcard p{font-size:12px;line-height:23px;color:#2b3042;margin-top:8px}
.arrow{position:absolute;top:3785px;width:36px;height:36px;border-radius:50%;display:flex;align-items:center;justify-content:center}

/* cta */
.cta{position:absolute;left:141px;top:3995px;width:916px;height:381px;border-radius:70px 20px 70px 20px;background:linear-gradient(90deg,#2458a8 0%,#6b4a88 50%,#ef4b1f 100%);overflow:hidden}
.cta-title{position:absolute;left:0;width:916px;top:74px;text-align:center;font-size:41px;line-height:46px;font-weight:500;color:var(--white);letter-spacing:.5px}
.cta-title em{font-family:"Playfair Display",serif;font-weight:500}
.cta-sub{position:absolute;left:0;width:916px;top:180px;text-align:center;font-size:12.5px;line-height:23px;color:var(--white)}
.cta-photo{position:absolute;clip-path:polygon(50% 0,100% 50%,50% 100%,0 50%)}

/* footer */
.footer{top:4460px;height:379px;background:var(--navy);color:var(--white)}
.f-brand{left:141px;top:4524px;font-family:"Lexend",sans-serif;font-size:36px;font-weight:600;letter-spacing:1px;display:flex;align-items:center;gap:10px}
.f-brand i{width:14px;height:14px;background:var(--orange);border-radius:3px;display:block}
.f-news{left:141px;top:4594px;font-size:11px;line-height:17px;width:300px}
.f-input{left:145px;top:4655px;width:260px;height:34px;border-radius:17px;background:var(--white);font-size:11px;color:#9aa0b4;padding-left:16px;line-height:34px}
.f-input span{position:absolute;right:4px;top:4px;width:26px;height:26px;border-radius:50%;background:var(--orange);display:flex;align-items:center;justify-content:center}
.f-col h4{font-size:17px;font-weight:500;margin-bottom:12px}
.f-col .l{font-size:12.5px;line-height:27px}
.f-contact{display:flex;gap:10px;font-size:12.5px;line-height:20px;margin-bottom:8px}
.f-contact svg{flex:none;margin-top:3px}
.f-social{display:flex;align-items:center;gap:12px;font-size:12.5px;margin-bottom:12px}
.f-social i{width:30px;height:30px;border-radius:50%;border:1.5px solid var(--white);display:block}
.f-social i.fill{background:var(--orange);border-color:var(--orange)}
.f-line{left:141px;top:4780px;width:916px;height:1px;background:rgba(255,255,255,.3)}
.f-copy{left:141px;top:4800px;font-size:11.5px}
.f-legal{right:143px;top:4800px;font-size:11.5px}
</style>
</head>
<body>

<!-- HERO -->
<section class="section hero">
  <div class="brand" style="left:140px;top:60px;font-size:26px"><span class="mark"></span>POLLBEACON</div>
  <nav class="nav"><span>PRODUCT</span><span>ABOUT</span><span>RESOURCES</span><span>PRICING</span><span>CONTACT</span></nav>
  <a class="btn btn-primary" style="left:766px;top:23px;width:150px;height:41px;background:var(--blue)">Request a demo</a>
  <a class="btn btn-outline" style="left:926px;top:23px;width:82px;height:41px">Login</a>
  <div class="lang">EN <span>| DA</span></div>

  <svg class="abs" style="left:218px;top:344px" width="28" height="28" viewBox="0 0 28 28"><path d="M4 2 L26 14 L4 26 Z" fill="#7a5ce6"/></svg>
  <svg class="abs" style="left:1030px;top:340px" width="40" height="40" viewBox="0 0 40 40"><path d="M6 30 A16 16 0 0 1 34 12" stroke="#f59a23" stroke-width="8" fill="none" stroke-linecap="round"/></svg>

  <h1 class="abs center hero-title">Transform Customer Experience<br>with <span class="accent">Data</span> + <span class="script">Expertise</span></h1>
  <p class="abs center hero-sub">PollBeacon combines powerful CX technology with expert consulting to<br>help you understand customers, reduce churn, and drive growth.</p>
  <a class="btn btn-primary" style="left:458px;top:333px;width:149px;height:48px">Request a demo</a>
  <a class="btn btn-outline" style="left:621px;top:333px;width:123px;height:48px">Learn more</a>
</section>

<!-- DASHBOARD -->
<div class="dash" role="img" aria-label="Analytics dashboard preview">
  <div class="side">
    <div class="brand"><span class="mark"></span>POLLBEACON</div>
    <div class="menu">
      <div class="on">Home</div><div>Invoices</div><div>Clients</div><div>Products</div><div>Messages</div><div>Settings</div><div>Help</div>
    </div>
    <div class="logout">Log Out</div>
  </div>
  <div class="search">Type to search</div>
  <div class="user"><i></i>Dana Ruel</div>

  <div class="stat" style="left:135px"><div class="lbl"><i style="background:var(--orange)"></i>Total Revenue</div><div class="val">$ 216k<em>+3.4</em></div></div>
  <div class="stat" style="left:250px"><div class="lbl"><i style="background:var(--orange)"></i>Invoices</div><div class="val">2,221<em>+2.8</em></div></div>
  <div class="stat" style="left:365px"><div class="lbl"><i style="background:var(--blue)"></i>Clients</div><div class="val">1,423<em>+1.1</em></div></div>
  <div class="stat" style="left:480px"><div class="lbl"><i style="background:var(--orange)"></i>Loyalty</div><div class="val">78%<em style="background:#fde3dc;color:var(--orange)">-0.2</em></div></div>

  <div class="chart-card">
    <div class="t">Monthly Revenue</div>
    <div class="v">$ 15,000</div>
    <svg width="260" height="120" viewBox="0 0 260 120" style="margin-top:6px">
      <g fill="#e6eaf4">
        <rect x="4" y="64" width="16" height="36" rx="3"/><rect x="32" y="74" width="16" height="26" rx="3"/>
        <rect x="88" y="60" width="16" height="40" rx="3"/><rect x="116" y="70" width="16" height="30" rx="3"/>
        <rect x="144" y="56" width="16" height="44" rx="3"/><rect x="172" y="68" width="16" height="32" rx="3"/>
        <rect x="200" y="62" width="16" height="38" rx="3"/><rect x="228" y="72" width="16" height="28" rx="3"/>
      </g>
      <rect x="60" y="52" width="16" height="48" rx="3" fill="var(--blue)"/>
      <rect x="50" y="24" width="38" height="16" rx="3" fill="#12151f"/>
      <text x="69" y="35" font-size="6" fill="#fff" text-anchor="middle">$15,000</text>
      <g font-size="5" fill="#9aa0b4" text-anchor="middle">
        <text x="12" y="112">Mar</text><text x="40" y="112">Apr</text><text x="68" y="112">May</text><text x="96" y="112">Jun</text><text x="124" y="112">Jul</text><text x="152" y="112">Aug</text><text x="180" y="112">Sep</text><text x="208" y="112">Oct</text><text x="236" y="112">Nov</text>
      </g>
    </svg>
  </div>

  <div class="promo">
    <span class="tag">New</span>
    <div class="h">We have added new invoicing templates!</div>
    <div class="p">New templates focused on helping you improve your business.</div>
    <div class="b">Download Now</div>
  </div>

  <div class="panel" style="left:135px;width:140px">
    <div class="t">Activities</div>
    <div class="act"><i style="background:#c5cbe0"></i><div><b>Hugo Ferris</b> created invoice PQ-4491C<br>Just now</div></div>
    <div class="act"><i style="background:#f5a623"></i><div>Invoice JL-3432B reminder was sent to <b>Bramble Co</b></div></div>
  </div>
  <div class="panel" style="left:290px;width:292px">
    <div class="t">Recent Invoices</div>
    <table class="inv">
      <tr><td>No</td><td>Date Created</td><td>Client</td><td>Amount</td><td>Status</td></tr>
      <tr><td>PQ-4491C</td><td>3 Jul, 2025</td><td>Rita Marsh</td><td>$2,480</td><td><span class="pill" style="background:#dff3e6;color:#2b9a55">Paid</span></td></tr>
      <tr><td>IN-9911J</td><td>21 May, 2025</td><td>Carl Monroe</td><td>$14,610</td><td><span class="pill" style="background:#fde3dc;color:var(--orange)">Overdue</span></td></tr>
    </table>
  </div>
</div>

<!-- TRUSTED -->
<h2 class="abs center trusted-title">TRUSTED BY INDUSTRY LEADERS</h2>
<div class="partners">
  <div class="partner"><i style="background:var(--orange)"></i>Northwind</div>
  <div class="partner"><i></i>Altura</div>
  <div class="partner"><i></i>Kestrel</div>
  <div class="partner"><i style="background:#1d2438"></i>Brightline</div>
  <div class="partner"><i style="background:#6a5ae0"></i>Orbitly</div>
  <div class="partner"><i style="background:#7fb5e8"></i>Tessera</div>
</div>

<!-- FEATURES -->
<h2 class="abs center sec-title feat-title">PollBeacon Features</h2>
<p class="abs center sec-sub feat-sub">Get the technology you need and the expertise you want. Our comprehensive approach delivers<br>measurable improvements in customer loyalty and retention.</p>

<div class="fcard" style="left:143px;top:1262px">
  <svg viewBox="0 0 66 62"><rect x="14" y="6" width="26" height="34" rx="3" fill="none" stroke="var(--blue)" stroke-width="3"/><path d="M20 16h14M20 23h14M20 30h9" stroke="var(--blue)" stroke-width="3"/><circle cx="46" cy="42" r="10" fill="none" stroke="var(--orange)" stroke-width="4"/><circle cx="46" cy="42" r="3" fill="var(--orange)"/></svg>
  <h3>Real-Time Feedback</h3>
  <p>Capture Customer Insights In Real-Time With Customizable Surveys And Feedback Tools.</p>
</div>
<div class="fcard" style="left:456px;top:1262px">
  <svg viewBox="0 0 66 62"><circle cx="33" cy="16" r="9" fill="none" stroke="var(--orange)" stroke-width="3"/><path d="M16 52c0-12 8-20 17-20s17 8 17 20" fill="none" stroke="var(--blue)" stroke-width="4"/><rect x="10" y="52" width="46" height="5" rx="2" fill="var(--blue)"/></svg>
  <h3>Expert Consulting</h3>
  <p>Access Instant Insights With Our Live Dashboards And Customizable Reports That Track Key CX Metrics.</p>
</div>
<div class="fcard" style="left:770px;top:1262px">
  <svg viewBox="0 0 66 62"><circle cx="28" cy="28" r="16" fill="none" stroke="var(--blue)" stroke-width="6" stroke-dasharray="7 4"/><circle cx="28" cy="28" r="6" fill="var(--blue)"/><path d="M46 34l12 22H34z" fill="var(--orange)"/><path d="M46 42v6" stroke="#fff" stroke-width="2.5"/></svg>
  <h3>Churn-Risk Alerts</h3>
  <p>Access Instant Insights With Our Live Dashboards And Customizable Reports That Track Key CX Metrics.</p>
</div>
<div class="fcard" style="left:143px;top:1508px">
  <svg viewBox="0 0 66 62"><circle cx="33" cy="22" r="14" fill="none" stroke="var(--blue)" stroke-width="4"/><path d="M33 8v14h14" fill="var(--orange)" stroke="var(--orange)" stroke-width="3"/><path d="M14 56c2-10 10-14 19-14s17 4 19 14" fill="none" stroke="var(--orange)" stroke-width="4"/></svg>
  <h3>Segment Insights</h3>
  <p>Dive Deep Into Customer Segments To Understand Different Needs And Behaviors.</p>
</div>
<div class="fcard" style="left:456px;top:1508px">
  <svg viewBox="0 0 66 62"><circle cx="33" cy="26" r="18" fill="none" stroke="var(--blue)" stroke-width="6" stroke-dasharray="8 4"/><circle cx="33" cy="24" r="6" fill="var(--orange)"/><path d="M22 40c2-6 6-8 11-8s9 2 11 8" fill="var(--orange)"/></svg>
  <h3>Leadership Reporting</h3>
  <p>Access Ready-To-Present Reports That Highlight Key Metrics And Insights.</p>
</div>
<div class="fcard" style="left:770px;top:1508px">
  <svg viewBox="0 0 66 62"><circle cx="26" cy="16" r="8" fill="none" stroke="var(--blue)" stroke-width="3"/><path d="M10 50c0-12 7-20 16-20" fill="none" stroke="var(--blue)" stroke-width="4"/><path d="M44 28l4 8 9 1-7 6 2 9-8-5-8 5 2-9-7-6 9-1z" fill="var(--orange)"/></svg>
  <h3>Loyalty Improvement</h3>
  <p>Strengthen Customer Relationships And Build Lasting Loyalty With Actionable Insights.</p>
</div>

<a class="btn btn-primary" style="left:458px;top:1771px;width:149px;height:48px">Request a demo</a>
<a class="btn btn-outline" style="left:621px;top:1771px;width:123px;height:48px">Learn more</a>

<!-- ABOUT -->
<section class="section about"></section>
<div class="about-photo" role="img" aria-label="Two colleagues reviewing customer data on a tablet"></div>
<div class="an-card">
  <div class="t">Sales Analytics</div>
  <div class="p">6.0% ↗</div>
  <svg width="115" height="50" viewBox="0 0 115 50" style="margin-top:8px">
    <rect x="2" y="24" width="9" height="26" rx="2" fill="var(--blue)"/><rect x="18" y="14" width="9" height="36" rx="2" fill="var(--blue)"/>
    <rect x="34" y="30" width="9" height="20" rx="2" fill="var(--blue)"/><rect x="50" y="20" width="9" height="30" rx="2" fill="var(--blue)"/>
    <rect x="66" y="8" width="9" height="42" rx="2" fill="var(--orange)"/><rect x="82" y="26" width="9" height="24" rx="2" fill="var(--blue)"/>
    <rect x="98" y="4" width="9" height="46" rx="2" fill="var(--blue)"/>
  </svg>
</div>
<div class="an-badge"></div>
<div class="rating">
  <i style="background:#7f8aa3"></i><i style="background:#b08a6a"></i><i style="background:#e8a23a"></i>
  <div class="txt"><div class="stars">★★★★★</div><div class="small">4.97 based <b>on 25 reviews</b></div></div>
</div>
<svg class="abs" style="left:535px;top:2270px" width="36" height="36" viewBox="0 0 36 36"><circle cx="18" cy="18" r="17" fill="var(--blue)"/><path d="M12 19l4 4 8-9" stroke="#fff" stroke-width="3" fill="none"/></svg>

<div class="abs about-kicker">ABOUT</div>
<h2 class="abs about-title">POLLBEACON</h2>
<div class="abs about-text">
  <p>Our mission is to empower businesses with the tools and expertise to build lasting customer relationships. Founded by CX innovators, we combine cutting-edge technology with human insights to drive measurable results.</p>
  <p>With over a decade of experience helping businesses transform their operations, we understand that every organization has unique challenges and goals. Our team of experts works closely with you to deliver solutions that not only meet your current needs but scale with your future growth.</p>
</div>
<a class="btn btn-primary" style="left:674px;top:2318px;width:153px;height:48px">Request a demo</a>
<a class="btn btn-outline" style="left:838px;top:2318px;width:123px;height:48px">Learn more</a>

<!-- WHY -->
<h2 class="abs center sec-title why-title">Why Choose PollBeacon?</h2>
<p class="abs center sec-sub why-sub">Discover the features that make our solution the right choice for businesses<br>looking to optimize their workflow and boost productivity.</p>

<svg class="abs" style="left:440px;top:2700px" width="320" height="300" viewBox="0 0 320 300">
  <g stroke="#b9c2da" stroke-width="1.5" fill="none">
    <path d="M0 46 H50 L90 86"/><path d="M320 46 H270 L230 86"/>
    <path d="M0 246 H50 L90 206"/><path d="M320 246 H270 L230 206"/>
  </g>
  <g fill="#fff" stroke="var(--blue)" stroke-width="2"><circle cx="90" cy="86" r="5"/><circle cx="230" cy="86" r="5"/><circle cx="90" cy="206" r="5"/><circle cx="230" cy="206" r="5"/></g>
  <rect x="95" y="81" width="130" height="130" rx="14" transform="rotate(45 160 146)" fill="none" stroke="var(--blue)" stroke-width="22"/>
</svg>

<div class="why-item" style="left:188px;top:2733px;text-align:right;width:184px">The Power Of Software<br>+ Expert Guidance</div>
<div class="why-icon b" style="left:389px;top:2714px"><svg width="28" height="28" viewBox="0 0 28 28"><rect x="3" y="5" width="22" height="15" rx="2" fill="none" stroke="#fff" stroke-width="2.5"/><path d="M9 24h10" stroke="#fff" stroke-width="2.5"/></svg></div>
<div class="why-icon o" style="left:744px;top:2714px"><svg width="28" height="28" viewBox="0 0 28 28"><path d="M3 14l6-5 5 4 5-4 6 5-11 9z" fill="none" stroke="#fff" stroke-width="2.5" stroke-linejoin="round"/></svg></div>
<div class="why-item" style="left:830px;top:2721px">Strengthen Relationships<br>At Every Touchpoint</div>
<div class="why-item" style="left:188px;top:2922px;text-align:right;width:184px">Move From Insight To<br>Action, Faster</div>
<div class="why-icon b" style="left:389px;top:2913px"><svg width="28" height="28" viewBox="0 0 28 28"><circle cx="14" cy="14" r="10" fill="none" stroke="#fff" stroke-width="2.5"/><path d="M14 8v6l4 3" stroke="#fff" stroke-width="2.5" fill="none"/></svg></div>
<div class="why-icon o" style="left:744px;top:2913px"><svg width="28" height="28" viewBox="0 0 28 28"><path d="M14 3l9 4v7c0 6-4 9-9 11-5-2-9-5-9-11V7z" fill="none" stroke="#fff" stroke-width="2.5"/><path d="M10 14l3 3 5-6" stroke="#fff" stroke-width="2.5" fill="none"/></svg></div>
<div class="why-item" style="left:825px;top:2922px">Protect Revenue And<br>Reduce Customer Churn</div>

<a class="btn btn-primary" style="left:458px;top:3047px;width:149px;height:48px">Request a demo</a>
<a class="btn btn-outline" style="left:621px;top:3047px;width:123px;height:48px">Learn more</a>

<!-- TESTIMONIALS -->
<section class="section testi"></section>
<h2 class="abs center sec-title testi-title">What Our Clients Say</h2>
<p class="abs center sec-sub testi-sub">Hear from businesses that have transformed their customer experience with PollBeacon.</p>

<div class="tcard" style="left:-167px">
  <div class="head"><div class="av" style="background:#2b9a55">R</div><div><div class="n">Rosa Kent</div><div class="c">Ferngate Group</div></div></div>
  <div class="stars">★★★★★</div>
  <p>Lorem Ipsum is simply dummy text of the printing and typesetting industry. Lorem Ipsum has been the industry's standard dummy text ever since</p>
</div>
<div class="tcard" style="left:139px">
  <div class="head"><div class="av" style="background:#4caf3a">J</div><div><div class="n">Martin Hale</div><div class="c">Corvid Systems</div></div></div>
  <div class="stars">★★★★★</div>
  <p>Lorem Ipsum is simply dummy text of the printing and typesetting industry. Lorem Ipsum has been the industry's standard dummy text ever since the 1500s, when an unknown printer took a galley of type and scrambled it to make a type specimen book. It has</p>
</div>
<div class="tcard" style="left:454px">
  <div class="head"><div class="av" style="background:#e53950">N</div><div><div class="n">Nora Briggs</div><div class="c">Lumen Works</div></div></div>
  <div class="stars">★★★★★</div>
  <p>Lorem Ipsum is simply dummy text of the printing and typesetting industry. Lorem Ipsum has been the industry's standard dummy text ever since the 1500s, when an unknown printer took a galley of type and scrambled it to make a type specimen book. It has survived not only five centuries, but also the leap into electronic typesetting</p>
</div>
<div class="tcard" style="left:770px">
  <div class="head"><div class="av" style="background:#f5b82a">A</div><div><div class="n">Alma Jensen</div><div class="c">Tidewater Labs</div></div></div>
  <div class="stars">★★★★★</div>
  <p>Lorem Ipsum is simply dummy text of the printing and typesetting industry. Lorem Ipsum has been the industry's standard dummy text ever since the 1500s, when an unknown printer took a galley of type and scrambled it to make a type specimen book. It has survived not only five centuries, but also</p>
</div>
<div class="tcard" style="left:1085px">
  <div class="head"><div class="av" style="background:#2a2f3d">L</div><div><div class="n">Leo Varga</div><div class="c">Parallax</div></div></div>
  <div class="stars">★★★★★</div>
  <p>Lorem Ipsum is simply dummy text of the printing and typesetting industry. Lorem Ipsum has been the industry's standard du</p>
</div>

<div class="arrow" style="left:559px;border:1.5px solid #1d2438;background:#fff"><svg width="14" height="14" viewBox="0 0 14 14"><path d="M12 7H2M6 3L2 7l4 4" stroke="#1d2438" stroke-width="1.6" fill="none"/></svg></div>
<div class="arrow" style="left:607px;background:var(--orange)"><svg width="14" height="14" viewBox="0 0 14 14"><path d="M2 7h10M8 3l4 4-4 4" stroke="#fff" stroke-width="1.6" fill="none"/></svg></div>

<!-- CTA -->
<div class="cta">
  <div class="cta-photo" role="img" aria-label="Consultant working on a laptop" style="left:-10px;top:127px;width:236px;height:236px;background:linear-gradient(135deg,#dcdfe6,#8c7f78 60%,#4d4b58)"></div>
  <div class="cta-photo" role="img" aria-label="Business professional with digital data icons" style="left:734px;top:80px;width:200px;height:200px;background:linear-gradient(135deg,#5a7fb8,#2b3f66 60%,#1b2440)"></div>
  <h2 class="cta-title">Ready to Transform<br>Your <em>Customer Experience?</em></h2>
  <p class="cta-sub">See how PollBeacon can help you collect better feedback, gain deeper insights, and<br>drive measurable improvements in customer loyalty.</p>
  <a class="btn" style="left:345px;top:245px;width:228px;height:44px;background:#fff;color:var(--ink);font-size:11.5px">Schedule your demo today</a>
</div>

<!-- FOOTER -->
<footer class="section footer"></footer>
<div class="abs f-brand" style="color:#fff"><i></i>POLLBEACON</div>
<p class="abs f-news" style="color:#fff">Latest Updates, Exclusive Content, And Special Offers? Subscribe To Our Newsletter!</p>
<div class="abs f-input">Your Email<span><svg width="12" height="12" viewBox="0 0 12 12"><path d="M1 6h10M7 2l4 4-4 4" stroke="#fff" stroke-width="1.6" fill="none"/></svg></span></div>

<div class="abs f-col" style="left:488px;top:4522px;color:#fff">
  <h4>Quick Links</h4>
  <div class="l">Home</div><div class="l">Product</div><div class="l">About</div><div class="l">Resources</div><div class="l">Pricing</div><div class="l">Contact</div>
</div>
<div class="abs f-col" style="left:678px;top:4522px;color:#fff;width:220px">
  <h4>Contact Details</h4>
  <div class="f-contact"><svg width="12" height="14" viewBox="0 0 12 14"><path d="M6 13s5-5 5-8A5 5 0 0 0 1 5c0 3 5 8 5 8z" fill="#fff"/><circle cx="6" cy="5" r="1.8" fill="var(--navy)"/></svg><div>48 Harbor Lane, Suite 210<br>Brookfield, WI 53005<br>United States</div></div>
  <div class="f-contact"><svg width="12" height="12" viewBox="0 0 12 12"><path d="M2 1h3l1 3-2 1a7 7 0 0 0 3 3l1-2 3 1v3c-6 0-9-3-9-9z" fill="#fff"/></svg><div>Phone<br>+1 555 014 2290</div></div>
  <div class="f-contact"><svg width="12" height="10" viewBox="0 0 12 10"><rect x="0.5" y="0.5" width="11" height="9" rx="1" fill="#fff"/><path d="M1 1l5 4 5-4" stroke="var(--navy)" fill="none"/></svg><div>Email<br>hello@pollbeacon.com</div></div>
</div>
<div class="abs f-col" style="left:940px;top:4522px;color:#fff">
  <h4>Social Media</h4>
  <div class="f-social"><i class="fill"></i>Friendwall</div>
  <div class="f-social"><i></i>Vidstream</div>
  <div class="f-social"><i></i>Worknet</div>
  <div class="f-social"><i></i>Snapgram</div>
</div>
<div class="abs f-line"></div>
<div class="abs f-copy" style="color:#fff">© 2025 PollBeacon. All Rights Reserved.</div>
<div class="abs f-legal" style="color:#fff">Privacy Policy | Terms Of Service</div>

</body>
</html>
```